Redesign Corporate website for BrightHarbor

We have an existing website that we ant to overhaul. We have a fair amount of content but are looking for bold design, graphics, lots of out of the box notions and ideas, really edgy stuff. We are a US government contractor really looking to push the envelope. We have some new logo options already completed but are open to new ideas as well. We want a complete multi page design and hosting preferably in AWS. We want a resource to manage our site, regularly developing and implementing new content and ideas. Would also prefer a resource who can also transform our web site into a full portfolio of digital and hard copy marketing materials. BrightHarbor (www.brightharborgroup.example) is a US goverbment contractor doing cloud services, agile development, mobility solutions, federated identity management, enterprise network operations.

Target Market(s)

US government agencies and US government contractors

Requirements
Must have
• Must be edgy and include must have moving graphics and pictures on the masthead and sound and motion each click or page change.

```html
<!DOCTYPE html>
<html lang="en">
<head>
<meta charset="utf-8">
<title>BrightHarbor</title>
<link rel="stylesheet" href="https://fonts.googleapis.com/css2?family=Arimo:wght@400;700&family=Source+Sans+3:wght@400;600&display=swap">
<style>
:root{
  --red:#e8262a;
  --ink:#333;
  --text:#555;
  --muted:#666;
  --white:#fff;
  --paper:#f0f0f0;
  --footer:#565656;
  --blue:#1b75bb;
  --band:#2a2f36;
}
*{margin:0;padding:0;box-sizing:border-box}
html,body{width:1200px;height:2812px;overflow:hidden}
body{position:relative;background:var(--white);font-family:"Arimo",Arial,sans-serif;color:var(--text)}
.abs{position:absolute}
.center{left:0;width:1200px;text-align:center}

/* header */
.site-header{top:0;left:0;width:1200px;height:118px;background:var(--white)}
.brand{left:88px;top:46px;display:flex;align-items:center;gap:12px}
.brand-dot{width:22px;height:22px;border-radius:50%;background:var(--red)}
.brand-name{font-size:38px;font-weight:400;color:#2b2b2b;letter-spacing:1px}
.main-nav{top:54px;left:600px;display:flex;font-size:18px;color:#222}
.main-nav a{color:inherit;text-decoration:none;height:34px;line-height:34px;margin-right:26px;padding:0 10px}
.main-nav a.active{background:var(--red);color:var(--white)}

/* hero */
.hero{top:118px;left:0;width:1200px;height:506px;background:linear-gradient(120deg,#6f8494 0%,#b7c7d2 35%,#8fa3b1 60%,#5b6d7b 100%)}
.hero-arrow{width:46px;height:46px;border-radius:50%;background:rgba(90,90,90,.55);top:268px}
.hero-caption{top:416px;left:0;width:1200px;height:90px;background:rgba(40,40,40,.45)}
.hero-caption h1{position:absolute;left:88px;top:28px;font-size:30px;font-weight:700;color:var(--white)}

/* core qualities */
.section-title{font-size:30px;font-weight:400;color:var(--red)}
.intro{left:94px;width:1012px;top:731px;font-size:14px;line-height:23px;text-align:center;color:var(--text)}
.quality{width:320px;text-align:center}
.quality-icon{width:80px;height:80px;border-radius:50%;background:var(--red);margin:0 auto;display:flex;align-items:center;justify-content:center}
.quality h3{font-size:22px;font-weight:400;color:#222;margin-top:24px}
.quality p{font-size:15px;line-height:22px;color:var(--text);margin-top:8px;letter-spacing:.5px}

/* mission band */
.mission{top:1078px;left:0;width:1200px;height:251px;background:linear-gradient(180deg,#20252c,#3b3f45 70%,#2c2f34)}
.mission p{position:absolute;top:54px;left:0;width:1200px;text-align:center;font-size:26px;line-height:44px;color:var(--white)}

/* feature */
.feature-visual{left:103px;top:1397px;width:338px;height:206px;background:linear-gradient(135deg,#e8efe8,#cfd8cf 50%,#2a2a2a 51%,#444);border-radius:6px}
.feature-title{left:499px;top:1396px;font-size:24px;color:var(--red)}
.feature-copy{left:499px;top:1437px;width:600px;font-family:"Source Sans 3",sans-serif;font-size:14px;line-height:22px;color:var(--muted)}
.feature-copy p+p{margin-top:12px}
.more-link{left:499px;top:1598px;font-family:"Source Sans 3",sans-serif;font-size:16px;color:#444;display:flex;align-items:center;gap:10px}

/* services */
.services{top:1682px;left:0;width:1200px;height:471px;background:var(--paper)}
.service{width:310px}
.service-photo{height:165px;border:6px solid var(--white);box-shadow:0 1px 3px rgba(0,0,0,.25)}
.service h3{font-family:"Source Sans 3",sans-serif;font-size:19px;font-weight:600;color:var(--red);margin-top:16px}
.service p{font-size:13.5px;line-height:25px;color:var(--text);margin-top:6px}
.btn{display:inline-block;margin-top:10px;background:var(--blue);color:var(--white);font-family:"Source Sans 3",sans-serif;font-size:14px;padding:0 14px;height:32px;line-height:32px}

/* team */
.member{width:360px;text-align:center}
.member-photo{width:176px;height:176px;border-radius:50%;margin:0 auto}
.member h4{font-size:18px;font-weight:400;color:#8a4a2a;margin-top:28px}
.member p{font-size:14px;line-height:25.5px;color:var(--ink);margin-top:8px}

/* footer */
.site-footer{top:2693px;left:0;width:1200px;height:119px;background:var(--footer);color:var(--white)}
.footer-links{position:absolute;left:88px;top:30px;font-size:14px}
.copyright{position:absolute;left:88px;top:68px;font-size:14px}
.social{position:absolute;top:52px;width:34px;height:34px}
</style>
</head>
<body>

<header class="abs site-header">
  <div class="abs brand"><span class="brand-name">BrightHarbor</span><span class="brand-dot"></span></div>
  <nav class="abs main-nav">
    <a class="active">HOME</a><a>ABOUT</a><a>SERVICES</a><a>CAREERS</a><a>CONTACT</a>
  </nav>
</header>

<section class="abs hero" role="img" aria-label="Blurred photo of business people shaking hands in a bright office">
  <div class="abs hero-arrow" style="left:89px"></div>
  <div class="abs hero-arrow" style="left:1066px"></div>
  <svg class="abs" style="left:89px;top:268px" width="46" height="46"><path d="M26 15 L18 23 L26 31" fill="none" stroke="#fff" stroke-width="2"/></svg>
  <svg class="abs" style="left:1066px;top:268px" width="46" height="46"><path d="M20 15 L28 23 L20 31" fill="none" stroke="#fff" stroke-width="2"/></svg>
  <div class="hero-caption"><h1>OPTIMIZING IT FOR CLIENT CRITICAL SOLUTIONS</h1></div>
</section>

<h2 class="abs center section-title" style="top:672px">OUR CORE QUALITIES</h2>
<p class="abs intro">Vivamus sagittis lacus vel augue laoreet rutrum faucibus dolor auctor. Aenean lacinia bibendum nulla sed consectetur. Because we think it's time for a new excite! Are you ready for an adventure to remember for a lifetime? Accusantium quaim, ultricies eget tempor id, aliquam eget nibh et. Maecen aliquairis</p>

<div class="abs quality" style="left:123px;top:826px">
  <div class="quality-icon"><svg width="40" height="40" viewBox="0 0 40 40" fill="none" stroke="#fff" stroke-width="2.5"><circle cx="20" cy="20" r="6"/><circle cx="20" cy="20" r="13" stroke-dasharray="5 4"/></svg></div>
  <h3>EXPERTISE</h3>
  <p>Lorem ipsum dolor sit amet adipis<br>msan. Morbi ut elit utipsum tristiquea<br>Pellentesque habitant morbi.</p>
</div>
<div class="abs quality" style="left:440px;top:826px">
  <div class="quality-icon"><svg width="40" height="40" viewBox="0 0 40 40" fill="#fff"><path d="M20 6 L33 12 L20 18 L7 12Z"/><path d="M7 15 L18 20 L18 34 L7 28Z"/><path d="M33 15 L22 20 L22 34 L33 28Z"/></svg></div>
  <h3>INNOVATION</h3>
  <p>Lorem ipsum dolor sit amet adipis<br>msan. Morbi ut elit utipsum tristiquea<br>Pellentesque habitant morbi.</p>
</div>
<div class="abs quality" style="left:757px;top:826px">
  <div class="quality-icon"><svg width="40" height="40" viewBox="0 0 40 40" fill="#fff"><circle cx="20" cy="16" r="10"/><rect x="15" y="24" width="10" height="6"/><rect x="16" y="31" width="8" height="3"/></svg></div>
  <h3>RESULTS</h3>
  <p>Lorem ipsum dolor sit amet adipis<br>msan. Morbi ut elit utipsum tristiquea<br>Pellentesque habitant morbi.</p>
</div>

<section class="abs mission" role="img" aria-label="Dusk photo of a city skyline with columns in the foreground">
  <p>WE ARE COMMITTED TO HELPING GOVERNMENTS<br>TRANSFORM IT TO SERVE, PROTECT AND MEET MISSION<br>CRITICAL INITIATIVES.</p>
</section>

<div class="abs feature-visual" role="img" aria-label="Dashboard software shown on desktop, tablet and phone screens"></div>
<h2 class="abs feature-title">Optimizing It For Mission Critical Solutions</h2>
<div class="abs feature-copy">
  <p>Vivamus sagittis lacus vel augue laoreet rutrum faucibus dolor auctor. Aenean lacinia bibendum nulla a sed consectetur. Because we think it's time for a new exciting challenge! Are you ready for an adventure to remember for a lifetime? Accusantium quam, ultricies eget tempor id, aliquam eget nibh et. Maecen aliquam, risus at sempe</p>
  <p>A program's rankings can be a key factor in choosing an accredited online college. Rankings provide an objective look at a program based on quantifiable factors, such as cost, graduation.</p>
</div>
<div class="abs more-link">READ MORE <svg width="14" height="14"><circle cx="7" cy="7" r="7" fill="#555"/><path d="M6 4 L9 7 L6 10" fill="none" stroke="#fff" stroke-width="1.6"/></svg></div>

<section class="abs services">
  <h2 class="abs center section-title" style="top:27px">OUR SERVICES</h2>
  <div class="abs service" style="left:86px;top:94px">
    <div class="service-photo" role="img" aria-label="Photo of people walking through a busy office" style="background:linear-gradient(135deg,#8fa0a8,#c8b9a3 50%,#6d6a63)"></div>
    <h3>SECURE MOBILITY SOLUTIONS</h3>
    <p>Claritas est etiam processus dynamicus, qui seqi uitur mutationem consuetudium lecitorum.Miru es t notare quam littera gothica, quam. Claritas.</p>
    <span class="btn">READ MORE</span>
  </div>
  <div class="abs service" style="left:446px;top:94px">
    <div class="service-photo" role="img" aria-label="Photo of an open hand beneath a drawn cloud" style="background:linear-gradient(180deg,#7fb2d6,#4d86b4 60%,#c9a48c)"></div>
    <h3>CLOUD ENABLEMENT</h3>
    <p>Claritas est etiam processus dynamicus, qui seqi uitur mutationem consuetudium lecitorum.Miru es t notare quam littera gothica, quam. Claritas.</p>
    <span class="btn">READ MORE</span>
  </div>
  <div class="abs service" style="left:804px;top:94px">
    <div class="service-photo" role="img" aria-label="Blue abstract image of light beams and puzzle pieces" style="background:linear-gradient(135deg,#0b2a6e,#2f6fd0 55%,#10307a)"></div>
    <h3>INTELLIGENCE ANALYSIS</h3>
    <p>Claritas est etiam processus dynamicus, qui seqi uitur mutationem consuetudium lecitorum.Miru es t notare quam littera gothica, quam. Claritas.</p>
    <span class="btn">READ MORE</span>
  </div>
</section>

<h2 class="abs center section-title" style="top:2200px">MEET OUR TEAM</h2>
<div class="abs member" style="left:58px;top:2284px">
  <div class="member-photo" role="img" aria-label="Portrait photo of a team member" style="background:radial-gradient(circle,#d9e3ea,#a7b7c4)"></div>
  <h4>JOHN DOE (LOREM IPSUM)</h4>
  <p>Vivamus vel eros eget magna volutpat sagittis.<br>Nulla faucibus nibh a magna tincidunt accumsan<br>hendrerit nunc facilisis. Curabitur et libero sit<br>amet ante hendrerit</p>
</div>
<div class="abs member" style="left:416px;top:2284px">
  <div class="member-photo" role="img" aria-label="Portrait photo of a team member" style="background:radial-gradient(circle,#e8f2f6,#b9d3de)"></div>
  <h4>JOHN DOE (LOREM IPSUM)</h4>
  <p>Vivamus vel eros eget magna volutpat sagittis.<br>Nulla faucibus nibh a magna tincidunt accumsan<br>hendrerit nunc facilisis. Curabitur et libero sit<br>amet ante hendrerit</p>
</div>
<div class="abs member" style="left:776px;top:2284px">
  <div class="member-photo" role="img" aria-label="Portrait photo of a team member" style="background:radial-gradient(circle,#eef0f0,#c3c8ca)"></div>
  <h4>JOHN DOE (LOREM IPSUM)</h4>
  <p>Vivamus vel eros eget magna volutpat sagittis.<br>Nulla faucibus nibh a magna tincidunt accumsan<br>hendrerit nunc facilisis. Curabitur et libero sit<br>amet ante hendrerit</p>
</div>

<footer class="abs site-footer">
  <div class="footer-links">Home | About | Meet The Team | Services | Our Values | Careers | Contact</div>
  <div class="copyright">Copyright © 2013. All Rights Reserved.</div>
  <span class="social" style="left:908px;background:#3b5998"></span>
  <span class="social" style="left:958px;background:#2aa9e0"></span>
  <span class="social" style="left:1006px;background:#f26522"></span>
  <span class="social" style="left:1056px;background:#e52d27"></span>
</footer>

</body>
</html>
```